Business Card Design Project

I require a business card with the following information on them for various different people;
name
m:
f:
e:
I have a logo already and will attached that. We are in the construction industry. I require something clean and simple but eye catching at the same time. You can use another colour with our logo if you like and you can style the logo as well if you wish. I am open.
Also it needs to be front and back design.
Industry/Entity Type
Construction
Requirements
Must have
- Logo, name, mobile, fax and email address.
Front and back design

```html
<!DOCTYPE html>
<html lang="en">
<head>
<meta charset="utf-8">
<title>Stonefield Developments – Business Card</title>
<link rel="stylesheet" href="https://fonts.googleapis.com/css2?family=Source+Sans+3:wght@400;600&display=swap">
<style>
  :root {
    --backdrop: #333a3d;
    --card: #ffffff;
    --brand-green: #55ee00;
    --ink-dark: #3a3f42;
    --icon-grey: #5a6066;
    --text-light: #ffffff;
    --skyline-dark: #1a1a1a;
    --skyline-mid: #4a4a4a;
  }
  * { margin: 0; padding: 0; box-sizing: border-box; }
  html, body {
    width: 1200px;
    height: 718px;
    overflow: hidden;
    background: var(--backdrop);
    font-family: "Source Sans 3", "Helvetica Neue", Arial, sans-serif;
  }
  .canvas {
    position: relative;
    width: 1200px;
    height: 718px;
    background: var(--backdrop);
  }
  .card-top-strip {
    position: absolute;
    left: 0; top: 150px;
    width: 975px; height: 27px;
    background: var(--card);
  }
  .card-body {
    position: absolute;
    left: 0; top: 177px;
    width: 1002px; height: 414px;
    background: var(--card);
  }
  .brand {
    position: absolute;
    left: 80px; top: 188px;
    display: flex;
    align-items: center;
    gap: 18px;
  }
  .brand-square {
    width: 56px; height: 56px;
    background: var(--brand-green);
  }
  .brand-name {
    font-size: 44px;
    font-weight: 400;
    color: var(--ink-dark);
    letter-spacing: 0.5px;
    line-height: 1;
  }
  .contact-panel {
    position: absolute;
    left: 0; top: 300px;
    width: 571px; height: 185px;
    background: var(--brand-green);
  }
  .contact-panel-tail {
    position: absolute;
    left: 0; top: 485px;
    width: 505px; height: 68px;
    background: var(--brand-green);
  }
  .chevrons {
    position: absolute;
    left: 78px; top: 418px;
    width: 44px; height: 28px;
  }
  .person-name {
    position: absolute;
    left: 234px; top: 312px;
    font-size: 26px;
    font-weight: 400;
    color: var(--text-light);
    letter-spacing: 0.3px;
  }
  .contact-line {
    position: absolute;
    left: 232px;
    font-size: 23px;
    font-weight: 600;
    color: var(--text-light);
    white-space: nowrap;
  }
  .contact-line.mobile { top: 356px; }
  .contact-line.fax { top: 401px; left: 234px; }
  .contact-line.email { top: 447px; left: 237px; }
  .contact-icon {
    position: absolute;
    left: 170px;
    width: 30px; height: 30px;
  }
  .contact-icon.phone { top: 354px; }
  .contact-icon.mail { top: 401px; }
  .contact-icon.globe { top: 448px; }
  .skyline {
    position: absolute;
    left: 627px; top: 303px;
    width: 337px; height: 251px;
    background: linear-gradient(180deg, var(--skyline-mid) 0%, var(--skyline-dark) 100%);
  }
</style>
</head>
<body>
<main class="canvas">
  <div class="card-top-strip"></div>
  <section class="card-body" aria-hidden="true"></section>

  <header class="brand">
    <div class="brand-square"></div>
    <span class="brand-name">Stonefield Developments</span>
  </header>

  <div class="contact-panel"></div>
  <div class="contact-panel-tail"></div>

  <svg class="chevrons" viewBox="0 0 44 28" aria-hidden="true">
    <polyline points="2,4 16,14 2,24" fill="none" stroke="var(--icon-grey)" stroke-width="5"/>
    <polyline points="20,4 34,14 20,24" fill="none" stroke="var(--text-light)" stroke-width="5"/>
  </svg>

  <p class="person-name">DANIEL HART</p>

  <svg class="contact-icon phone" viewBox="0 0 30 30" aria-hidden="true">
    <path d="M7 3 L12 3 L14 10 L11 12 Q14 18 19 20 L21 17 L28 19 L28 24 Q26 28 21 27 Q8 23 3 9 Q3 4 7 3 Z" fill="var(--icon-grey)"/>
  </svg>
  <p class="contact-line mobile">m: 0761-3358-204</p>

  <svg class="contact-icon mail" viewBox="0 0 30 30" aria-hidden="true">
    <rect x="1" y="5" width="28" height="20" fill="var(--icon-grey)"/>
    <polyline points="2,6 15,17 28,6" fill="none" stroke="var(--brand-green)" stroke-width="2"/>
  </svg>
  <p class="contact-line fax">f:&nbsp; 0208-145-0937</p>

  <svg class="contact-icon globe" viewBox="0 0 30 30" aria-hidden="true">
    <circle cx="15" cy="15" r="13" fill="var(--icon-grey)"/>
    <g fill="none" stroke="var(--brand-green)" stroke-width="1.4">
      <ellipse cx="15" cy="15" rx="6" ry="13"/>
      <line x1="15" y1="2" x2="15" y2="28"/>
      <line x1="2" y1="15" x2="28" y2="15"/>
      <line x1="4" y1="9" x2="26" y2="9"/>
      <line x1="4" y1="21" x2="26" y2="21"/>
    </g>
  </svg>
  <p class="contact-line email">e: daniel@stonefield.com</p>

  <div class="skyline" role="img" aria-label="Black and white illustration of city skyscrapers seen from below"></div>
</main>
</body>
</html>
```